Bramwell Dental personal information forms

We are a Dental Practice that require an update to our information forms, there are 3 versions of it.
I will attach our old ones, we need to keep the same information on there, we just want them to look better and use our current logo and colours.
Our website is www.bramwelldental-example.net
Our facebook is www.facebook.com/bramwelldentalkestonwalk/
..................................................................................................

Target Market(s)

Everyone, easy to read

Industry/Entity Type

Dental Clinic

Colors
0692cd
34a6d7
cee9f5
ffffff
0255a3
3276b5

Requirements
Must have
• Logo
• Our colours
• same information as the uploaded versions
Should not have
• any other colour besides the blues, black and white

```html
<!DOCTYPE html>
<html lang="en">
<head>
<meta charset="UTF-8">
<title>Bramwell Dental – Medical History Update Form</title>
<link href="https://fonts.googleapis.com/css2?family=Jost:ital,wght@0,400;0,500;0,600;0,700;1,400&display=swap" rel="stylesheet">
<style>
  :root {
    --blue-deep: #0255a3;
    --blue-mid: #3276b5;
    --blue-bright: #0692cd;
    --blue-light: #34a6d7;
    --blue-pale: #cee9f5;
    --white: #ffffff;
    --ink: #111111;
    --field: #ececec;
    --rule: #e2e2e2;
    --backdrop: #e6e8ea;
  }
  * { box-sizing: border-box; margin: 0; padding: 0; }
  html, body { width: 1200px; height: 1200px; overflow: hidden; }
  body {
    background: var(--backdrop);
    font-family: "Jost", sans-serif;
    color: var(--ink);
    position: relative;
  }
  .form-sheet {
    position: absolute;
    left: 210px; top: 48px;
    width: 780px; height: 1104px;
    background: var(--white);
  }
  .masthead {
    position: absolute; left: 0; top: 0; width: 100%; height: 100px;
    background: radial-gradient(ellipse at 50% 60%, var(--blue-light) 0%, var(--blue-bright) 45%, var(--blue-deep) 100%);
    display: flex; align-items: center; justify-content: center;
  }
  .brand-name {
    color: var(--white); font-weight: 500; font-size: 42px; letter-spacing: 0.5px;
  }
  .masthead-rule {
    position: absolute; left: 0; top: 104px; width: 100%; height: 6px;
    background: linear-gradient(90deg, var(--blue-deep), var(--blue-bright) 50%, var(--blue-deep));
  }
  .practitioner {
    position: absolute; left: 22px; top: 164px;
    color: var(--blue-deep); font-weight: 700; font-size: 16px; line-height: 20px;
  }
  .sticker-box {
    position: absolute; left: 473px; top: 152px; width: 285px; height: 60px;
    border: 1px solid var(--rule);
    display: flex; align-items: center; justify-content: center;
    font-style: italic; font-size: 14px;
  }
  .welcome {
    position: absolute; left: 22px; top: 262px;
    color: var(--blue-deep); font-size: 16px;
  }
  .intro {
    position: absolute; left: 22px; top: 283px; width: 740px;
    font-size: 16px; line-height: 19.5px;
  }
  .intro strong { font-weight: 700; }

  .history-table {
    position: absolute; left: 20px; top: 388px; width: 740px; height: 525px;
    border: 1px solid var(--rule);
    font-size: 12px;
    display: flex; flex-direction: column;
  }
  .question {
    display: flex; justify-content: space-between; align-items: flex-start;
    padding: 6px 8px 0 10px; line-height: 15px;
  }
  .answer-choice { font-weight: 700; font-size: 12px; }
  .answer-field { background: var(--field); height: 23px; }
  .conditions { height: 212px; padding: 10px 10px 0 10px; }
  .conditions-title { line-height: 15px; margin-bottom: 10px; }
  .conditions-grid {
    display: grid; grid-template-columns: 236px 241px 1fr; padding-left: 16px;
  }
  .condition-list { list-style: none; }
  .condition-list li {
    display: flex; align-items: center; height: 17.6px; font-size: 12px;
  }
  .tick-box {
    width: 8px; height: 8px; margin-right: 11px;
    border: 1px solid #222; box-shadow: -1.5px 1.5px 0 #222;
  }

  .declaration {
    position: absolute; left: 22px; top: 953px; width: 748px;
    font-weight: 700; font-size: 12px; line-height: 15px;
  }
  .sign-row {
    position: absolute; left: 22px; top: 996px;
    display: flex; align-items: flex-end; font-size: 12px;
  }
  .sign-line { display: inline-block; border-bottom: 1px solid #888; margin-left: 8px; height: 12px; }
  .sign-line.signature { width: 133px; margin-right: 40px; }
  .sign-line.date { width: 133px; }
  .footer-band {
    position: absolute; left: 0; bottom: 0; width: 100%; height: 30px;
    background: radial-gradient(ellipse at 50% 50%, var(--blue-light) 0%, var(--blue-bright) 45%, var(--blue-deep) 100%);
  }
</style>
</head>
<body>
  <main class="form-sheet">
    <header class="masthead">
      <span class="brand-name">Bramwell Dental</span>
    </header>
    <div class="masthead-rule"></div>

    <div class="practitioner">Dr.Henry Calloway<br>Dental Surgeon</div>
    <div class="sticker-box">Affix patient sticker here.</div>

    <p class="welcome">Welcome back to our practice!</p>
    <p class="intro"><strong>THIS INFORMATION IS CONFIDENTIAL</strong> and is necessary to enable us to offer you <strong>THE BEST POSSIBLE</strong> CARE.It is now mandatory to have a written updated medical history every 2 years and we would apprecaite your time in thoroughly completing this form.</p>

    <section class="history-table">
      <div class="question" style="height:44px"><span>Are you currently or have you taken any prescribed medication or dietary supplements in the last 12 months?<br>(If YES please list below)</span><span class="answer-choice">YES/NO</span></div>
      <div class="answer-field"></div>

      <div class="question" style="height:37px"><span>Allergies / Reactions?<br>(If YES please list below)</span><span class="answer-choice">YES/NO</span></div>
      <div class="answer-field"></div>

      <div class="conditions">
        <p class="conditions-title">Have you ever had or are you suffering from any of the following? Please tick any that apply :</p>
        <div class="conditions-grid">
          <ul class="condition-list">
            <li><span class="tick-box"></span>Rheumatic fever</li>
            <li><span class="tick-box"></span>Epilepsy</li>
            <li><span class="tick-box"></span>Asthma</li>
            <li><span class="tick-box"></span>Tuberculosis</li>
            <li><span class="tick-box"></span>Radiation Therapy</li>
            <li><span class="tick-box"></span>Dizziness, fainting</li>
            <li><span class="tick-box"></span>Hepatitis A B or C</li>
            <li><span class="tick-box"></span>Recent eye surgery</li>
          </ul>
          <ul class="condition-list">
            <li><span class="tick-box"></span>Diabetes</li>
            <li><span class="tick-box"></span>kidney disease</li>
            <li><span class="tick-box"></span>Heart attack</li>
            <li><span class="tick-box"></span>High Blood Pressure</li>
            <li><span class="tick-box"></span>Bleeding problems</li>
            <li><span class="tick-box"></span>Artificial joints</li>
            <li><span class="tick-box"></span>Respiratory Problems</li>
          </ul>
          <ul class="condition-list">
            <li><span class="tick-box"></span>HIV Positive</li>
            <li><span class="tick-box"></span>High cholesterol</li>
            <li><span class="tick-box"></span>Cancer</li>
            <li><span class="tick-box"></span>Pace-maker</li>
            <li><span class="tick-box"></span>Osteoporosis</li>
            <li><span class="tick-box"></span>Heart rate problems</li>
            <li><span class="tick-box"></span>Heart murmur</li>
          </ul>
        </div>
      </div>

      <div class="question" style="height:22px"><span>Do you have any disease,condition or problem not lited above?</span><span class="answer-choice">YES/NO</span></div>
      <div class="answer-field"></div>

      <div class="question" style="height:22px"><span>Have you had surgery or been to hospital in the last 5 years? (If YES,Please give details)</span><span class="answer-choice">YES/NO</span></div>
      <div class="answer-field" style="height:21px"></div>

      <div class="question" style="height:20px"><span>For Women:Are you pregnant? (If YES, How many months?)</span><span class="answer-choice">YES/NO</span></div>
      <div class="answer-field" style="height:22px"></div>

      <div class="question" style="height:21px"><span>Do you currently or have you ever smoked?</span><span class="answer-choice">YES/NO</span></div>
      <div class="answer-field"></div>
    </section>

    <p class="declaration">The information that I have provided is to the best of my knowledge true and I understand that is my responsibility to inform of any changes in my medical status.</p>
    <div class="sign-row">
      <span>Patient/Parent/Person Responsible signature:</span><span class="sign-line signature"></span>
      <span>Date:</span><span class="sign-line date"></span>
    </div>

    <footer class="footer-band"></footer>
  </main>
</body>
</html>
```